Business Card Design Project

I need a business card designed with these details on the front along with the logo attached on the front.

Address - 518/ 207 Wendover st Pellbrook
Website - www.quarrelinebuilders.com.au
Email - tavin@quarrelinebuilders.com.au
Fax - 1900 417 652
Mobile - 0471936058
Telephone - 1300527961
Licence number - 874062k

```html
<!DOCTYPE html>
<html lang="en">
<head>
<meta charset="utf-8">
<title>Quarreline Builders – Business Card</title>
<link rel="stylesheet" href="https://fonts.googleapis.com/css2?family=Tinos:wght@700&family=Ubuntu:wght@400&display=swap">
<style>
  :root {
    --page: #2b2b2b;
    --brown: #4a2820;
    --cream: #fbe9dc;
    --ink: #4a2820;
    --light: #f6e6da;
    --tile: #e9ddc9;
  }
  html, body {
    margin: 0;
    width: 1200px;
    height: 900px;
    overflow: hidden;
    background: var(--page);
  }
  .card {
    position: absolute;
    left: 122px;
    top: 157px;
    width: 955px;
    height: 585px;
    border-radius: 0 45px 0 45px;
    overflow: hidden;
    background: var(--cream);
    box-shadow: 0 6px 18px rgba(0,0,0,.45);
  }
  .card__top {
    position: absolute;
    inset: 0 0 auto 0;
    height: 369px;
    background: var(--brown);
  }
  .licence {
    position: absolute;
    right: 52px;
    top: 50px;
    font: 400 18px/1 "Ubuntu", sans-serif;
    color: var(--light);
  }
  .brand__tile {
    position: absolute;
    left: 52px;
    top: 112px;
    width: 149px;
    height: 149px;
    background: var(--tile);
  }
  .brand__name {
    position: absolute;
    left: 230px;
    top: 112px;
    margin: 0;
    font: 700 54px/72px "Tinos", "Times New Roman", serif;
    color: var(--light);
    letter-spacing: 1px;
  }
  .contact {
    position: absolute;
    top: 417px;
    margin: 0;
    padding: 0;
    list-style: none;
    font: 400 27px/36px "Ubuntu", sans-serif;
    color: var(--ink);
  }
  .contact--left { left: 54px; }
  .contact--right { left: 672px; }
  .contact li { display: flex; align-items: center; gap: 8px; white-space: nowrap; }
  .contact svg { width: 20px; height: 20px; fill: var(--ink); flex: none; }
  .divider {
    position: absolute;
    left: 632px;
    top: 414px;
    bottom: 0;
    width: 2px;
    background: var(--ink);
  }
</style>
</head>
<body>
  <div class="card">
    <div class="card__top">
      <span class="licence">Licence number - 874062k</span>
      <div class="brand__tile"></div>
      <h1 class="brand__name">QUARRELINE<br>BUILDERS</h1>
    </div>

    <ul class="contact contact--left">
      <li><svg viewBox="0 0 20 20"><path d="M10 1a6 6 0 0 0-6 6c0 5 6 12 6 12s6-7 6-12a6 6 0 0 0-6-6zm0 8.5a2.5 2.5 0 1 1 0-5 2.5 2.5 0 0 1 0 5z"/></svg>518/ 207 Wendover st Pellbrook</li>
      <li><svg viewBox="0 0 20 20"><path d="M2 5h16v10H2z M2 5l8 6 8-6" fill="none" stroke="#4a2820" stroke-width="0"/><path d="M2 5h16l-8 6z"/><path d="M2 7l8 6 8-6v8H2z"/></svg>tavin@quarrelinebuilders.com.au</li>
      <li><svg viewBox="0 0 20 20"><circle cx="10" cy="10" r="8" fill="none" stroke="#4a2820" stroke-width="2"/><path d="M2 10h16M10 2c-4 4-4 12 0 16M10 2c4 4 4 12 0 16" fill="none" stroke="#4a2820" stroke-width="1.6"/></svg>www.quarrelinebuilders.com.au</li>
    </ul>

    <div class="divider"></div>

    <ul class="contact contact--right">
      <li><svg viewBox="0 0 20 20"><path d="M5 2h10v5H5z"/><path d="M2 8h16v7h-3v3H5v-3H2z"/></svg>1900 417 652</li>
      <li><svg viewBox="0 0 20 20"><path d="M6 1h8a1 1 0 0 1 1 1v16a1 1 0 0 1-1 1H6a1 1 0 0 1-1-1V2a1 1 0 0 1 1-1zm1 2v12h6V3z"/></svg>0471 936 058</li>
      <li><svg viewBox="0 0 20 20"><path d="M5 2l3 4-2 2c1 3 3 5 6 6l2-2 4 3-2 3C9 18 2 11 2 4z" fill="none" stroke="#4a2820" stroke-width="1.6"/></svg>1300 527 961</li>
    </ul>
  </div>
</body>
</html>
```